K & T Fabrication Web Design | ||
Web Template | ||
Manufacturing | ||
www.kandtfab.example | ||
The current business that I am purchasing is a run of the mill, precision metal machining and manufacturing company. The owner is retirement age and it's my objective to make it new school and cutting edge. I want professional, eye catching concepts that capture what I am trying to do with the traditionally old school industry. I want to appeal to the younger engineers in the industry. I want to illustrate the professional, cutting edge services I intend to offer through my company. I want to show that we are not the traditional, dirty old machine shop. We are a company run by a young, fast-paced engineer focused on providing the highest quality work in the industry. | ||
I would like to have a navigation bar that contains "HOME", "CAPABILITIES", "PROJECTS", "ABOUT US", and "CONTACT US" tabs. I like un-cluttered websites that deliver a clear message that the company has an organized, structured leadership in place. I want to show that the machining industry is not always old, dirty, and antiquated. My company is cutting edge, engineering driven, and able to meet the customer's every demand. | ||
Cutting-Edge Unique/Creative Clean/Simple Professional Sophisticated Modern Industrial Progressive High Tech Masculine |
Black/Charcoal | ||
above header | ||
http://www.pellworth-clinical.example/ | ||
http://world.varnick-ostley.example/master/6600.htm | ||
http://brockmoorlifts.example/ | ||
Please attempt to match font type of the uploaded business card and company logo designs. I would like to have a seamless design throughout. | ||

```html
<!DOCTYPE html>
<html lang="en">
<head>
<meta charset="utf-8">
<title>K &amp; T Fabrication</title>
<link href="https://fonts.googleapis.com/css2?family=Arimo:wght@400;700&family=Exo+2:wght@400;600&display=swap" rel="stylesheet">
<style>
:root{
  --bg-dark:#1c1d1f;
  --bg-darker:#141516;
  --panel:#2a2b2e;
  --line:#3a3b3f;
  --blue:#1e82d6;
  --blue-dark:#125ea3;
  --text-light:#d9dadc;
  --text-mute:#8b8d92;
  --text-body:#555;
  --heading:#333;
  --white:#fff;
  --page:#f3f3f3;
}
*{box-sizing:border-box;margin:0;padding:0}
html,body{width:1200px;height:971px;overflow:hidden}
body{position:relative;background:var(--page);font-family:"Arimo",Arial,sans-serif;color:var(--text-body)}
.abs{position:absolute}

/* header */
.site-header{left:0;top:0;width:1200px;height:128px;background:linear-gradient(#262729,var(--bg-dark))}
.brand{left:155px;top:20px;width:300px;height:100px}
.brand-mark{position:absolute;left:90px;top:0;width:70px;height:70px;border-radius:50%;background:#3c3e42}
.brand-name{position:absolute;left:0;top:80px;font-family:"Exo 2",sans-serif;font-size:26px;font-weight:600;color:var(--white);letter-spacing:.5px;white-space:nowrap}
.call{left:590px;top:14px;width:200px;height:50px}
.call-icon{position:absolute;left:0;top:0;width:40px;height:46px}
.call-label{position:absolute;left:48px;top:4px;font-size:17px;font-style:italic;color:var(--blue);font-weight:700}
.call-number{position:absolute;left:48px;top:26px;font-size:16px;color:var(--white);font-weight:700}
.search{left:842px;top:30px;width:192px;height:26px;background:#e9e9e9;border:1px solid #555;font-size:13px;color:#888;padding:5px 8px}
.search svg{position:absolute;right:-2px;top:0}
.nav{left:530px;top:92px;height:32px;display:flex}
.nav a{display:block;height:32px;line-height:32px;padding:0 22px;font-size:14px;font-weight:700;color:var(--white);text-decoration:none;letter-spacing:.5px}
.nav a.active{background:#3b4048;color:var(--blue);border-bottom:3px solid var(--blue)}

/* hero */
.hero{left:0;top:128px;width:1200px;height:252px;background:var(--bg-darker)}
.hero-photo{left:155px;top:128px;width:487px;height:252px;background:linear-gradient(135deg,#3c4550,#1a2028 60%,#55606a)}
.hero-copy{left:642px;top:128px;width:403px;height:252px;background:linear-gradient(#1d2c3c,#0f1822)}
.hero-title{position:absolute;left:8px;top:22px;font-family:"Exo 2",sans-serif;font-size:25px;color:var(--blue);line-height:30px}
.hero-title span{display:block;padding-left:100px}
.hero-text{position:absolute;left:8px;top:88px;width:385px;font-size:11.5px;line-height:15px;color:#9aa6b2}
.btn-more{position:absolute;right:20px;top:200px;height:28px;line-height:28px;padding:0 14px;background:var(--blue);color:var(--white);font-size:13px;font-weight:700}
.dots{left:158px;top:354px;display:flex;gap:6px}
.dots i{width:9px;height:9px;border-radius:50%;background:#777}
.dots i:first-child{background:var(--white)}

/* intro */
.intro-icon{left:158px;top:400px;width:60px;height:60px;border-radius:50%;background:#4a4d52}
.intro-title{left:235px;top:410px;font-size:28px;font-weight:700;color:var(--heading)}
.intro-text{left:235px;top:445px;width:560px;font-size:12.5px;line-height:16px;color:#555}

/* columns */
.card{top:495px;width:288px;height:295px;background:var(--white);box-shadow:0 0 6px rgba(0,0,0,.18)}
.card h2{font-size:22px;font-weight:400;color:var(--heading);padding:14px 14px 10px;border-bottom:1px solid #ddd}
.list{list-style:none;padding:4px 14px}
.list li{font-size:12.5px;color:#555;height:31px;line-height:31px;border-bottom:1px dotted #ccc}
.list li::before{content:"+";color:#333;font-weight:700;margin-right:10px}
.view-more{position:absolute;right:18px;bottom:14px;font-size:12px;color:var(--blue)}
.project-photo{margin:10px 14px 0;height:96px;background:linear-gradient(#b9cde0,#8c7a66 60%,#6f7a5a)}
.card p{font-size:12.5px;line-height:15px;color:var(--blue);padding:8px 14px}
.slider-dots{position:absolute;left:0;right:0;bottom:14px;display:flex;justify-content:center;gap:6px}
.slider-dots i{width:9px;height:9px;border-radius:50%;background:#ccc}
.slider-dots i:first-child{background:var(--blue)}
.person{display:flex;gap:10px;padding:10px 14px 0}
.person-photo{width:70px;height:82px;background:linear-gradient(#8a6d5a,#3d3e46)}
.person-name{font-family:Georgia,serif;font-size:13px;font-weight:700;color:#333}
.person-role{font-size:11px;font-style:italic;color:#777;margin-top:4px}

/* footer */
.site-footer{left:0;top:800px;width:1200px;height:171px;background:linear-gradient(#2a2b2d,#1b1c1e)}
.foot-brand{left:180px;top:818px;font-family:"Exo 2",sans-serif;font-size:32px;font-weight:600;color:#3e4044;white-space:nowrap}
.foot-tag{left:182px;top:862px;font-size:10px;color:#4a4c50;letter-spacing:1px}
.news-title{left:532px;top:840px;font-size:16px;color:var(--text-light)}
.news-input{left:532px;top:866px;width:206px;height:20px;background:#cfd0d2;font-size:11px;color:#666;padding:3px 6px}
.news-btn{left:532px;top:890px;width:64px;height:20px;background:var(--blue);color:var(--white);font-size:11px;text-align:center;line-height:20px}
.qc-title{left:836px;top:812px;font-size:14px;color:var(--text-light)}
.qc-text{left:836px;top:834px;font-size:11px;line-height:14px;color:var(--text-mute)}
.follow{left:836px;top:888px;font-size:14px;color:var(--text-light)}
.social{left:836px;top:908px;display:flex;gap:6px}
.social i{width:14px;height:14px;background:#5a6068}
.foot-rule{left:155px;top:940px;width:890px;height:1px;background:var(--line)}
.copyright{left:158px;top:948px;font-size:12px;color:var(--text-mute)}
.foot-nav{right:158px;top:948px;font-size:12px;color:var(--text-mute);word-spacing:4px}
</style>
</head>
<body>

<header class="abs site-header"></header>
<div class="abs brand">
  <div class="brand-mark"></div>
  <div class="brand-name">K &amp; T FABRICATION</div>
</div>
<div class="abs call">
  <svg class="call-icon" viewBox="0 0 40 46"><rect x="10" y="2" width="20" height="40" rx="4" fill="#1e82d6"/><rect x="13" y="7" width="14" height="24" fill="#0c3a66"/><circle cx="20" cy="37" r="2.5" fill="#0c3a66"/></svg>
  <div class="call-label">Call us at</div>
  <div class="call-number">(555) 014-2870</div>
</div>
<div class="abs search">Search...
  <svg width="26" height="26" viewBox="0 0 26 26"><rect width="26" height="26" fill="#1c1d1f"/><circle cx="11" cy="11" r="5" fill="none" stroke="#fff" stroke-width="2"/><line x1="15" y1="15" x2="20" y2="20" stroke="#fff" stroke-width="2.5"/></svg>
</div>
<nav class="abs nav">
  <a class="active" href="#">HOME</a><a href="#">CAPABILITIES</a><a href="#">PROJECTS</a><a href="#">ABOUT US</a><a href="#">CONTACT US</a>
</nav>

<section class="abs hero"></section>
<div class="abs hero-photo" role="img" aria-label="Photo of a precision-built engine bay with blue intake"></div>
<div class="abs hero-copy">
  <h1 class="hero-title">PRECISION PRODUCTS &amp;<span>ENGINEERED SOLUTIONS</span></h1>
  <p class="hero-text">Lorem ipsum dolor sit amet, consectetur adipiscing elit, sed do eiusmod tempor incididunt ut labore et dolore magna aliqua. Ut enim ad minim veniam, quis nostrud exercitation ullamco laboris nisi ut aliquip ex ea commodo consequat. Duis aute irure dolor in reprehenderit in voluptate velit esse cillum dolore eu fugiat nulla pariatur. Excepteur sint occaecat cupidatat non proident, sunt in culpa qui officia deserunt mollit anim id est laborum.</p>
  <div class="btn-more">View More &#9656;</div>
</div>
<div class="abs dots"><i></i><i></i><i></i><i></i></div>

<div class="abs intro-icon"></div>
<h2 class="abs intro-title">Who is K &amp; T Fabrication?</h2>
<p class="abs intro-text">We are a turn-key shop that provides precision products and engineered solutions. We specialize in custom prototyping, tool and die, welding, and automated assembly.</p>

<article class="abs card" style="left:158px">
  <h2>Our Products</h2>
  <ul class="list">
    <li>Lorem ipsum dolor sit amet, consectetur.</li>
    <li>Lorem ipsum dolor sit amet, consectetur.</li>
    <li>Lorem ipsum dolor sit amet, consectetur.</li>
    <li>Lorem ipsum dolor sit amet, consectetur.</li>
    <li>Lorem ipsum dolor sit amet, consectetur.</li>
    <li>Lorem ipsum dolor sit amet, consectetur.</li>
    <li>Lorem ipsum dolor sit amet, consectetur.</li>
  </ul>
  <div class="view-more">View more &#9656;</div>
</article>
<article class="abs card" style="left:456px">
  <h2>Our Current Projects</h2>
  <div class="project-photo" role="img" aria-label="Photo of an industrial plant with smokestacks"></div>
  <p>Lorem ipsum dolor sit amet, consectetur adipiscing elit, sed do eiusmod tempor incididunt ut labore et dolore magna aliqua. Ut enim ad minim veniam.</p>
  <div class="slider-dots"><i></i><i></i><i></i><i></i></div>
</article>
<article class="abs card" style="left:754px">
  <h2>Testimonials</h2>
  <div class="person">
    <div class="person-photo" role="img" aria-label="Portrait of the client"></div>
    <div><div class="person-name">M. Dana Holt</div><div class="person-role">Chair Person</div></div>
  </div>
  <p>Lorem ipsum dolor sit amet, consectetur adipiscing elit, sed do eiusmod tempor incididunt ut labore et dolore magna aliqua. Ut enim ad minim veniam.</p>
  <div class="slider-dots"><i></i><i></i><i></i><i></i></div>
</article>

<footer class="abs site-footer"></footer>
<div class="abs foot-brand">K &amp; T FABRICATION</div>
<div class="abs foot-tag">PRECISION PRODUCTS &amp; ENGINEERED SOLUTIONS</div>
<div class="abs news-title">Subscribe Newsletter</div>
<div class="abs news-input">Enter your email</div>
<div class="abs news-btn">Submit</div>
<div class="abs qc-title">Quick Contact</div>
<div class="abs qc-text">Email: info@kandtfab.example<br>Phone: (555) 014-2870</div>
<div class="abs follow">Follow us on</div>
<div class="abs social"><i></i><i></i><i></i><i></i><i></i></div>
<div class="abs foot-rule"></div>
<div class="abs copyright">Copyright (C) 2001, K &amp; T FABRICATION</div>
<div class="abs foot-nav">Home | Capabilities | Projects | About us | Contact us</div>

</body>
</html>
```